Brochure required for large legal practice

We require a brochure, poster and PowerPoint to be designed to promote our new Employee Benefits Program to our employees. The brochure needs to be modern, clean and corporate. Our target market is solicitors, legal support staff and administration staff based across multiple sites in Queensland, Australia. Logos and brochure/poster content have been attached as well as a detailed brief.

Please note that several photos of our employees have now been uploaded and can be used in this material only.                             

Legal

```html
<!DOCTYPE html>
<html lang="en">
<head>
<meta charset="utf-8">
<title>Harlow Group – Employee Benefits Program Poster</title>
<link href="https://fonts.googleapis.com/css2?family=Oswald:wght@400;500;600&display=swap" rel="stylesheet">
<style>
  :root {
    --backdrop: #e9e9e9;
    --paper: #ffffff;
    --ink-dark: #161616;
    --ink-mid: #2c2c2c;
    --brand-green: #5db85a;
    --text-white: #ffffff;
    --photo-strip: #1f1f1f;
  }
  * { margin: 0; padding: 0; box-sizing: border-box; }
  html, body {
    width: 872px; height: 1200px; overflow: hidden;
    background: var(--backdrop);
    font-family: "Oswald", "Arial Narrow", sans-serif;
  }
  .poster {
    position: absolute; left: 36px; top: 68px;
    width: 800px; height: 1063px;
    background: var(--paper);
    box-shadow: 0 14px 30px rgba(0,0,0,0.28);
  }
  .poster-field {
    position: absolute; left: 23.6px; top: 23.6px;
    width: 608px; height: 818px;
    transform: scale(1.2403); transform-origin: top left;
    background: radial-gradient(ellipse at 50% 40%, var(--ink-mid) 0%, var(--ink-dark) 75%);
    overflow: hidden;
  }
  .brand {
    position: absolute; left: 208px; top: 36px;
    color: var(--text-white);
  }
  .brand-mark {
    position: absolute; left: 0; top: 2px;
    width: 62px; height: 62px;
    border: 3px solid var(--text-white);
  }
  .brand-name {
    position: absolute; left: 83px; top: -4px;
    font-weight: 400; font-size: 32px; line-height: 36px;
    letter-spacing: 1px; white-space: nowrap; text-transform: uppercase;
  }
  .brand-tagline {
    position: absolute; left: 84px; top: 71px;
    font-weight: 400; font-size: 13px; line-height: 16px; white-space: nowrap;
  }
  .poster-title {
    position: absolute; left: 0; top: 160px; width: 100%;
    text-align: center; color: var(--brand-green);
    font-weight: 600; font-size: 44px; line-height: 56px;
  }
  .photo-strip {
    position: absolute; left: 0; top: 234px; width: 608px; height: 352px;
    background: var(--photo-strip);
  }
  .photo { position: absolute; }
  .photo--leaders   { left: 0;   top: 238px; width: 268px; height: 172px; background: linear-gradient(135deg, #2f63b0, #1d3f7a); }
  .photo--colleagues{ left: 278px; top: 238px; width: 103px; height: 172px; background: linear-gradient(180deg, #e8e6e0, #bdb8ae); }
  .photo--dining    { left: 391px; top: 238px; width: 217px; height: 172px; background: linear-gradient(135deg, #f2efea, #c9a88a 60%, #8a5a3c); }
  .photo--finance   { left: 0;   top: 419px; width: 268px; height: 69px;  background: linear-gradient(90deg, #0d1f3a, #27477a 60%, #c46a2a); }
  .photo--team      { left: 278px; top: 419px; width: 166px; height: 69px;  background: linear-gradient(180deg, #d9dadb, #8f9398); }
  .photo--holiday   { left: 455px; top: 419px; width: 153px; height: 162px; background: linear-gradient(180deg, #7e98b4 0%, #f0c070 45%, #e08a2a 65%, #3a2a1e 100%); }
  .photo--social    { left: 0;   top: 497px; width: 143px; height: 84px;  background: linear-gradient(180deg, #cfd0cc, #6a6a66); }
  .photo--travel    { left: 152px; top: 497px; width: 115px; height: 84px;  background: linear-gradient(180deg, #e6e8ea, #9ea3a8); }
  .photo--shopping  { left: 278px; top: 497px; width: 166px; height: 84px;  background: linear-gradient(135deg, #f4f2f3, #e59ac0 60%, #c65a8e); }
  .benefit-lines {
    position: absolute; left: 0; top: 612px;
    color: var(--brand-green); font-weight: 400; font-size: 24px; line-height: 38px;
    white-space: nowrap;
  }
  .benefit-lines p:nth-child(1) { padding-left: 36px; }
  .benefit-lines p:nth-child(2) { padding-left: 78px; }
  .benefit-lines p:nth-child(3) { padding-left: 155px; }
  .poster-footnote {
    position: absolute; left: 0; top: 764px; width: 100%;
    text-align: center; color: var(--text-white);
    font-weight: 500; font-size: 10px; line-height: 14px; white-space: nowrap;
  }
</style>
</head>
<body>
  <div class="poster">
    <div class="poster-field">
      <div class="brand">
        <div class="brand-mark"></div>
        <div class="brand-name">Harlow<br>Group</div>
        <div class="brand-tagline">working together</div>
      </div>

      <h1 class="poster-title">Employee Benefits Program</h1>

      <div class="photo-strip"></div>
      <div class="photo photo--leaders" role="img" aria-label="Two senior leaders shaking hands in front of a blue company sign"></div>
      <div class="photo photo--colleagues" role="img" aria-label="Two colleagues reading a folder in an office corridor"></div>
      <div class="photo photo--dining" role="img" aria-label="Plated restaurant meals on a dining table"></div>
      <div class="photo photo--finance" role="img" aria-label="Financial chart on a screen"></div>
      <div class="photo photo--team" role="img" aria-label="Group of four office staff standing together"></div>
      <div class="photo photo--holiday" role="img" aria-label="Two deck chairs on a beach at sunset"></div>
      <div class="photo photo--social" role="img" aria-label="Staff relaxing together on a sofa"></div>
      <div class="photo photo--travel" role="img" aria-label="Business travellers with luggage in an airport"></div>
      <div class="photo photo--shopping" role="img" aria-label="Friends holding shopping bags"></div>

      <div class="benefit-lines">
        <p>Offering you a range benefits...</p>
        <p>to support you physically, mentally and financially...</p>
        <p>and reward and recognise your achievements.</p>
      </div>

      <p class="poster-footnote">To find out more please see the Harlow Group Employee Benefits Program brochure or contact a member of the Human Resources team.</p>
    </div>
  </div>
</body>
</html>
```